Security Camera Sign

14” high x 11” wide Color: Blue, Yellow, Black and white

Make the sign vertical
Replace red with blue
WARNING: Black over yellow
These premises are protected by Closed Circuit Television: On white
Images are recorded for crime prevention and public safety. Unauthorized access, theft or vandalism will result in prosecution: On Blue

Target Market(s)

Outdoor commercial building

Industry/Entity Type

Security

Requirements
Nice to have
• I would like the sign stand out. If you need more colors? Thanks Ok

```html
<!DOCTYPE html>
<html lang="en">
<head>
<meta charset="utf-8">
<title>Security Camera Warning Sign</title>
<link rel="stylesheet" href="https://fonts.googleapis.com/css2?family=Bebas+Neue&family=Montserrat:wght@800&display=swap">
<style>
  :root {
    --sign-blue: #00a2e6;
    --sign-yellow: #fff200;
    --sign-ink: #2a2422;
    --sign-white: #ffffff;
    --camera-light: #dfe2e2;
    --camera-dark: #a9adad;
  }
  html, body {
    margin: 0;
    padding: 0;
    width: 947px;
    height: 1200px;
    overflow: hidden;
    background: var(--sign-white);
  }
  .sign {
    display: block;
    width: 947px;
    height: 1200px;
  }
  .sign-frame { fill: var(--sign-ink); }
  .sign-field { fill: var(--sign-blue); }
  .notice-band { fill: var(--sign-white); }
  .warning-plate { fill: var(--sign-ink); }
  .warning-panel { fill: var(--sign-yellow); }
  .warning-word {
    font-family: "Montserrat", sans-serif;
    font-weight: 800;
    font-size: 132px;
    fill: var(--sign-ink);
  }
  .cctv-statement {
    font-family: "Bebas Neue", sans-serif;
    font-size: 82px;
    fill: var(--sign-white);
  }
  .legal-notice {
    font-family: "Bebas Neue", sans-serif;
    fill: var(--sign-blue);
  }
  .legal-notice.large { font-size: 88px; }
  .legal-notice.medium { font-size: 76px; }
  .legal-notice.small { font-size: 60px; }
</style>
</head>
<body>
<svg class="sign" viewBox="0 0 947 1200" xmlns="http://www.w3.org/2000/svg">
  <defs>
    <linearGradient id="camera-tone" x1="0" y1="0" x2="1" y2="1">
      <stop offset="0" stop-color="var(--camera-light)"/>
      <stop offset="1" stop-color="var(--camera-dark)"/>
    </linearGradient>
    <clipPath id="sign-inner">
      <rect x="15" y="15" width="917" height="1170" rx="62"/>
    </clipPath>
  </defs>

  <rect class="sign-frame" x="0" y="0" width="947" height="1200" rx="76"/>

  <g clip-path="url(#sign-inner)">
    <rect class="sign-field" x="15" y="15" width="917" height="1170"/>
    <rect class="notice-band" x="15" y="761" width="917" height="345"/>
  </g>

  <rect class="camera-illustration" role="img" aria-label="Illustration of a wall-mounted CCTV security camera"
        x="420" y="42" width="488" height="498" rx="12" fill="url(#camera-tone)"/>

  <rect class="warning-plate" x="31" y="309" width="697" height="165" rx="32"/>
  <rect class="warning-panel" x="49" y="327" width="659" height="127" rx="14"/>
  <text class="warning-word" x="86" y="438" textLength="593" lengthAdjust="spacingAndGlyphs">WARNING</text>

  <text class="cctv-statement" x="70" y="634" textLength="789" lengthAdjust="spacingAndGlyphs">THESE PREMISES ARE PROTECTED</text>
  <text class="cctv-statement" x="97" y="703" textLength="734" lengthAdjust="spacingAndGlyphs">BY CLOSED CIRCUIT TELEVISION</text>

  <text class="legal-notice medium" x="84" y="855" textLength="777" lengthAdjust="spacingAndGlyphs">IMAGES ARE RECORDED FOR CRIME</text>
  <text class="legal-notice large" x="84" y="932" textLength="779" lengthAdjust="spacingAndGlyphs">PREVENTION AND PUBLIC SAFETY.</text>
  <text class="legal-notice medium" x="84" y="998" textLength="777" lengthAdjust="spacingAndGlyphs">UNAUTHORIZED ACCESS, THEFT OR</text>
  <text class="legal-notice small" x="88" y="1067" textLength="771" lengthAdjust="spacingAndGlyphs">VANDALISM WILL RESULT IN PROSECUTION</text>
</svg>
</body>
</html>
```